Four different size banners for our website

Hello,

I need four different size banners for our website :

728px x 90px
300px x 250px
160px x 600px
468px x 68px

All animated gifs with 3 slides no bigger than 50kb.

We would like to advertise following headlines :

1 )CO2 System Aquarium Specialists

2) Free Worldwide Shipping, Free Returns & Free Setup Advice

3) Create your CO2 System. OUR STEP-BY-STEP GUIDE MAKES IT SIMPLE TO GET STARTED

Logo attached.

You can view our website here : www.fernvalelab.co.uk

```html
<!DOCTYPE html>
<html lang="en">
<head>
<meta charset="utf-8">
<title>Fernvale Lab – CO2 System Aquarium Specialists</title>
<link href="https://fonts.googleapis.com/css2?family=Arimo:wght@700&display=swap" rel="stylesheet">
<style>
  :root {
    --brand-black: #111111;
    --brand-green: #3aa335;
    --leaf-green: #7cc242;
    --paper: #ffffff;
    --frame: #d6d6d6;
    --tank-deep: #1f4a3a;
    --tank-mid: #4f8f3a;
    --tank-light: #9fcf7a;
    --steel-light: #f2f3f5;
    --steel-mid: #c9ced6;
  }
  * { box-sizing: border-box; margin: 0; padding: 0; }
  html, body { width: 1200px; height: 148px; overflow: hidden; background: var(--paper); }
  .banner {
    position: relative;
    width: 1200px;
    height: 148px;
    background: var(--paper);
    border: 1px solid var(--frame);
    font-family: "Arimo", Arial, sans-serif;
    overflow: hidden;
  }
  .brand-panel {
    position: absolute;
    left: 0; top: 0;
    width: 304px; height: 148px;
  }
  .brand-name {
    position: absolute;
    left: 26px; top: 50%;
    transform: translateY(-50%);
    display: flex;
    align-items: center;
    gap: 12px;
    color: var(--paper);
    font-size: 34px;
    font-weight: 700;
    white-space: nowrap;
  }
  .brand-dot {
    width: 16px; height: 16px;
    border-radius: 50%;
    background: var(--leaf-green);
    flex: none;
  }
  .headline {
    position: absolute;
    left: 343px; top: 16px;
    color: var(--brand-green);
    font-size: 34px;
    font-weight: 700;
    line-height: 42px;
  }
  .tank-photo {
    position: absolute;
    left: 634px; top: 0;
    width: 356px; height: 148px;
    background: linear-gradient(180deg, var(--tank-deep) 0%, var(--tank-mid) 55%, var(--tank-light) 100%);
  }
  .product-photo {
    position: absolute;
    left: 1004px; top: 8px;
    width: 188px; height: 132px;
    background: radial-gradient(ellipse at 50% 45%, var(--steel-light) 0%, var(--steel-mid) 100%);
    border-radius: 8px;
  }
</style>
</head>
<body>
  <div class="banner">
    <svg class="brand-panel" viewBox="0 0 304 148" aria-hidden="true">
      <polygon points="0,0 280,0 304,74 280,148 0,148" fill="var(--brand-black)"/>
    </svg>
    <div class="brand-name"><span class="brand-dot"></span>Fernvale Lab</div>

    <h1 class="headline">CO2 System<br>Aquarium<br>Specialists</h1>

    <div class="tank-photo" role="img" aria-label="Planted aquarium with green stem plants, carpet plants and small fish"></div>
    <div class="product-photo" role="img" aria-label="CO2 pressure regulator with two gauges and a blue solenoid valve"></div>
  </div>
</body>
</html>
```